Silver Heron Construction Services

Create a business card for my business consulting company
Danielle Vesk, Founder and CEO
4816 Alder Brook Way, Ste 100
Denver, CO. 80451
303.782.4190 cell
dvesk@silverheronconst.example
www.silverheronconst.example

Target Market(s)

Private Equity and Construction Companies

Industry/Entity Type

Business / Sales Consulting

Contact Information for Business Card

Tag Line that says "Where The Road To Success Is Always Under Construction"

Requirements
Must have
• Logo on both sides of the card.
Nice to have
• Add tagline to the same side of the card as my name and contact info

```html
<!DOCTYPE html>
<html lang="en">
<head>
<meta charset="utf-8">
<title>Silver Heron Construction Services – Business Card</title>
<link rel="stylesheet" href="https://fonts.googleapis.com/css2?family=Poppins:wght@400;600;700&display=swap">
<style>
  :root {
    --backdrop: #2a2a2b;
    --card-light: #ffffff;
    --card-dark: #141414;
    --ink: #111111;
    --ink-soft: #222222;
    --rule: #9a9a9a;
    --paper-text: #f4f4f4;
    --pattern-top: #2b2b2d;
    --pattern-bottom: #0d0d0d;
  }
  * { box-sizing: border-box; margin: 0; padding: 0; }
  html, body {
    width: 1200px; height: 1108px; overflow: hidden;
    background: var(--backdrop);
    font-family: "Poppins", sans-serif;
  }
  .stage {
    position: relative; width: 1200px; height: 1108px;
    display: flex; justify-content: center; align-items: center; gap: 60px;
  }
  .card {
    width: 440px; height: 760px; border-radius: 30px;
    position: relative; overflow: hidden;
    box-shadow: 0 18px 40px rgba(0,0,0,0.45);
  }
  .card-front {
    background: var(--card-light); color: var(--ink);
    display: flex; flex-direction: column; align-items: center;
    padding: 90px 40px 0; text-align: center;
  }
  .brand-mark {
    display: flex; align-items: center; gap: 14px;
    height: 260px; justify-content: center;
  }
  .brand-dot { width: 22px; height: 22px; border-radius: 50%; background: var(--ink); flex: none; }
  .brand-name {
    font-weight: 700; font-size: 34px; line-height: 1.1; color: var(--ink);
    text-transform: uppercase; text-align: left;
  }
  .person-name { font-weight: 700; font-size: 30px; margin-top: 50px; letter-spacing: 0.5px; }
  .person-role { font-weight: 400; font-size: 24px; margin-top: 2px; color: var(--ink-soft); }
  .rule { width: 300px; height: 1px; background: var(--rule); margin: 14px 0; }
  .contact-icons { display: flex; gap: 8px; margin-bottom: 8px; }
  .contact-icon { width: 32px; height: 32px; border-radius: 5px; background: var(--ink); display: flex; align-items: center; justify-content: center; }
  .contact-line { font-size: 21px; line-height: 1.35; color: var(--ink-soft); }
  .contact-line.small { font-size: 18.5px; }
  .card-back { background: var(--card-dark); }
  .pattern-field {
    position: absolute; inset: 0;
    background: linear-gradient(160deg, var(--pattern-top), var(--pattern-bottom));
  }
  .back-sign {
    position: absolute; left: 0; right: 0; bottom: 110px;
    display: flex; flex-direction: column; align-items: center; gap: 26px;
  }
  .back-brand { display: flex; align-items: center; gap: 10px; }
  .back-brand .brand-dot { background: var(--paper-text); width: 14px; height: 14px; }
  .back-brand-name { color: var(--paper-text); font-weight: 700; font-size: 18px; text-transform: uppercase; }
  .tagline {
    color: var(--paper-text); font-size: 21px; font-weight: 400;
    text-transform: uppercase; text-align: center; line-height: 1.4; letter-spacing: 0.5px;
  }
</style>
</head>
<body>
<main class="stage">
  <section class="card card-front">
    <div class="brand-mark">
      <span class="brand-dot"></span>
      <span class="brand-name">Silver Heron<br>Construction Services</span>
    </div>
    <h1 class="person-name">DANIELLE VESK</h1>
    <p class="person-role">Founder and CEO</p>
    <div class="rule"></div>
    <div class="contact-icons">
      <span class="contact-icon">
        <svg width="20" height="20" viewBox="0 0 24 24"><path fill="#fff" d="M6.6 10.8a15 15 0 0 0 6.6 6.6l2.2-2.2a1 1 0 0 1 1-.25 11.4 11.4 0 0 0 3.6.6 1 1 0 0 1 1 1V20a1 1 0 0 1-1 1A17 17 0 0 1 3 4a1 1 0 0 1 1-1h3.5a1 1 0 0 1 1 1c0 1.25.2 2.45.6 3.6a1 1 0 0 1-.25 1z"/></svg>
      </span>
      <span class="contact-icon">
        <svg width="20" height="20" viewBox="0 0 24 24"><rect x="3" y="5" width="18" height="14" rx="1" fill="none" stroke="#fff" stroke-width="2"/><path d="M3 6l9 7 9-7" fill="none" stroke="#fff" stroke-width="2"/></svg>
      </span>
      <span class="contact-icon">
        <svg width="20" height="20" viewBox="0 0 24 24"><circle cx="12" cy="12" r="9" fill="none" stroke="#fff" stroke-width="2"/><path d="M3 12h18M12 3c3 3 3 15 0 18M12 3c-3 3-3 15 0 18" fill="none" stroke="#fff" stroke-width="1.6"/></svg>
      </span>
    </div>
    <p class="contact-line">303.782.4190</p>
    <p class="contact-line small">dvesk@silverheronconst.example</p>
    <p class="contact-line small">www.silverheronconst.example</p>
    <div class="rule"></div>
    <p class="contact-line">4816 Alder Brook Way</p>
    <p class="contact-line">Ste 100 Denver, CO. 80451</p>
  </section>

  <section class="card card-back">
    <div class="pattern-field" role="img" aria-label="Repeating tone-on-tone brand emblem pattern in glossy black"></div>
    <div class="back-sign">
      <div class="back-brand">
        <span class="brand-dot"></span>
        <span class="back-brand-name">Silver Heron</span>
      </div>
      <p class="tagline">The road to success is<br>always under construction</p>
    </div>
  </section>
</main>
</body>
</html>
```